Premium men's gut health supplement needs a bottle label designed

We’re velnora - a premium men’s wellness brand focused on gut health. Our first product is a high-quality daily supplement designed to support digestion, regularity, and internal cleanliness. Backed by science and tailored for modern lifestyles, velnora is crafted in the UK and proudly LGBT-owned. It aims to resolve intimacy problems that gay men may experience due to poor digestion but also does not exclude any other orientation - other men may use it simply to improve their digestion.

velnora is for health-conscious men who value science-backed supplements and want to feel confident from the inside out. Many of our early adopters will be gay and bisexual men who prioritise gut health as part of their self-care, sexual, and hygiene routine, though the product is equally effective and appealing to anyone seeking premium digestive support.

The product is premium the target customer is male, not specific to one location but primary markets will be US, UK and EU.

I’d like a supplement bottle designed for velnora, our premium men’s gut health brand. The focus should be clean, slightly clinical, and minimal - inspired by brands like Quelrin and Darvo. The key element is the wordmark (velnora) on the front, with no additional logo or icon. Lowercase text and a strong, contemporary font are preferred.

The bottle should be aesthetically pleasing so that people are proud to display it on their shelf, instead of hiding it in a cupboard (like Quelrin, darvo, Pia Venturek, Morvanel etc)

Avoid anything that shows the product as being for LGBT, e.g., no rainbows, men holding hands etc.

The design should be premium, minimalist and not be busy or overwhelming.

I have uploaded a file called "Bottle" to give an idea of the type of container, but please ignore the colours and change as you see fit. This is just for reference for the type of bottle we'll use - all colours are customisable.

I have also uploaded some images for "style" reference, e.g., darvo, quelrin, pia venturek, etc for inspiration.

```html
<!DOCTYPE html>
<html lang="en">
<head>
<meta charset="utf-8">
<title>velnora — digestive support label</title>
<link href="https://fonts.googleapis.com/css2?family=Libre+Baskerville:wght@700&family=Montserrat:wght@300;400;600&display=swap" rel="stylesheet">
<style>
  :root {
    --page: #ffffff;
    --label-dark: #1f1f1f;
    --label-mid: #3a3a3a;
    --label-edge: #2a2a2a;
    --ink: #f2f2f2;
    --ink-soft: #d6d6d6;
  }
  html, body {
    margin: 0;
    padding: 0;
    width: 1200px;
    height: 1200px;
    overflow: hidden;
    background: var(--page);
  }
  .label {
    position: absolute;
    left: 180px;
    top: 90px;
    width: 840px;
    height: 1020px;
    background: radial-gradient(ellipse at 48% 45%, var(--label-mid) 0%, var(--label-dark) 55%, var(--label-edge) 100%);
    color: var(--ink);
    font-family: "Montserrat", sans-serif;
  }
  .wordmark {
    position: absolute;
    top: 48px;
    left: 0;
    width: 100%;
    text-align: center;
    font-family: "Libre Baskerville", serif;
    font-weight: 700;
    font-size: 118px;
    letter-spacing: -3px;
    line-height: 1;
    margin: 0;
  }
  .product-name {
    position: absolute;
    top: 352px;
    left: 0;
    width: 100%;
    text-align: center;
    margin: 0;
    line-height: 1.02;
  }
  .product-name .category {
    display: block;
    font-weight: 600;
    font-size: 60px;
    letter-spacing: -0.5px;
  }
  .product-name .benefit {
    display: block;
    font-weight: 300;
    font-size: 66px;
    letter-spacing: 0;
  }
  .claim-box {
    position: absolute;
    top: 614px;
    left: 243px;
    width: 354px;
    height: 112px;
    box-sizing: border-box;
    border: 1.5px solid var(--ink-soft);
    display: flex;
    align-items: center;
    padding: 0 14px 0 16px;
    gap: 12px;
  }
  .claim-icon {
    width: 52px;
    height: 74px;
    border-radius: 6px;
    background: linear-gradient(180deg, #4a4a4a, #3c3c3c);
    flex: none;
  }
  .claim-text {
    font-weight: 300;
    font-size: 37px;
    line-height: 1.08;
    color: var(--ink-soft);
    text-align: center;
    flex: 1;
  }
  .net-weight {
    position: absolute;
    top: 880px;
    left: 0;
    width: 100%;
    text-align: center;
    font-weight: 400;
    font-size: 27px;
    color: var(--ink-soft);
    margin: 0;
  }
</style>
</head>
<body>
  <main class="label">
    <h1 class="wordmark">velnora</h1>
    <h2 class="product-name">
      <span class="category">digestive</span>
      <span class="benefit">support</span>
    </h2>
    <div class="claim-box">
      <div class="claim-icon" role="img" aria-label="Line icon of a stomach"></div>
      <div class="claim-text">internal<br>cleanliness</div>
    </div>
    <p class="net-weight">Net Weight: 60 Capsules</p>
  </main>
</body>
</html>
```